Outdoor sign for Brindle Auto Restoration

I need a horizontal 4'x 8' outdoor roadside sign for my classic auto restoration business. I have uploaded colors and our logo. Needs the Brindle name, a prominent Classic AUTO RESTORATION, phone number and website. We rebuild and restore vintage cars, trucks and 4x4s. I'd like something clean but possibly retro. Classic Auto Restoration is more important than the Brindle name. It needs to be visible and readable from the street. NO CLIP ART

Target Market(s)

Customers who need their vintage care restored or upgraded. Men and women ages 25-75

Industry/Entity Type

Automotive

Colors
FFC000
F8CF3A
FAE287
FDF2CF
FEFAEE

Requirements
Must have
• Legible. Bright. Readable as a backlit 4' x 8' large horizontal sign (roughly 120cm X 240cm)
Nice to have
• Use of the Brindle logo/type, Complete or Classic before prominent AUTO RESTORATION
Should not have
• Clip art of old cars or icons. And we don't want the Brindle Logo from the website because it wont be legible from the road. I have included the Illustrator file for Brindle text in the uploads

```html
<!DOCTYPE html>
<html lang="en">
<head>
<meta charset="utf-8">
<title>Brindle Auto Restoration – Roadside Sign</title>
<link rel="stylesheet" href="https://fonts.googleapis.com/css2?family=Archivo:wdth,wght@62..125,900&family=Roboto+Condensed:wght@700&display=swap">
<style>
  :root {
    --backdrop: #939598;
    --sign-black: #2b2828;
    --sign-black-light: #363232;
    --gold: #FFC000;
    --ink: #231f20;
    --white: #ffffff;
  }
  html, body {
    margin: 0;
    padding: 0;
    width: 1200px;
    height: 681px;
    overflow: hidden;
    background: var(--backdrop);
  }
  .sign {
    position: absolute;
    left: 80px;
    top: 81px;
    width: 1038px;
    height: 519px;
    background: radial-gradient(ellipse at 40% 35%, var(--sign-black-light), var(--sign-black) 70%);
    box-shadow: 8px 10px 10px rgba(0, 0, 0, 0.35);
  }
  .sign svg { display: block; }
  .headline {
    font-family: "Archivo", "Arial Black", sans-serif;
    font-weight: 900;
    font-stretch: 75%;
    font-size: 128px;
  }
  .headline-shadow { fill: var(--white); stroke: var(--ink); stroke-width: 3; paint-order: stroke; }
  .headline-face { fill: var(--gold); stroke: var(--ink); stroke-width: 5; paint-order: stroke; }
  .tagline-band { fill: var(--white); }
  .tagline {
    font-family: "Roboto Condensed", "Arial Narrow", sans-serif;
    font-weight: 700;
    font-size: 72px;
    fill: var(--ink);
  }
  .brand-name {
    font-family: "Archivo", "Arial Black", sans-serif;
    font-weight: 900;
    font-stretch: 75%;
    font-size: 134px;
    fill: var(--gold);
  }
  .contact {
    font-family: "Roboto Condensed", "Arial Narrow", sans-serif;
    font-weight: 700;
    font-size: 54px;
    fill: var(--white);
  }
  .contact-divider { fill: var(--gold); }
</style>
</head>
<body>
  <div class="sign">
    <svg width="1038" height="519" viewBox="0 0 1038 519" aria-label="Brindle Auto Restoration sign">
      <g class="headline">
        <text class="headline-shadow" x="29" y="137" textLength="988" lengthAdjust="spacingAndGlyphs">AUTO RESTORATION</text>
        <text class="headline-face" x="23" y="131" textLength="988" lengthAdjust="spacingAndGlyphs">AUTO RESTORATION</text>
      </g>

      <rect class="tagline-band" x="0" y="175" width="1038" height="87"/>
      <text class="tagline" x="23" y="241" textLength="987" lengthAdjust="spacingAndGlyphs">Restoring Vintage Cars, Trucks &amp; 4x4s</text>

      <text class="brand-name" x="519" y="394" text-anchor="middle" textLength="540" lengthAdjust="spacingAndGlyphs">BRINDLE</text>

      <text class="contact" x="32" y="476" textLength="303" lengthAdjust="spacingAndGlyphs">501-555-0142</text>
      <circle class="contact-divider" cx="391" cy="459" r="9.5"/>
      <text class="contact" x="449" y="476" textLength="558" lengthAdjust="spacingAndGlyphs">brindle autoworks.com</text>
    </svg>
  </div>
</body>
</html>
```